Packaging Design for High end coffee beans

The name is Cafe de Marvela.

I need this design to be amended you are welcome to design your own too.

We sell high end coffee beans from Colombia this needs to be reflected in the packaging.

The colour is black and Gold. i need the lettering to be fully gold not a fade.

It is to be printed on coffee packaging so the clarity and quality has to be ready for that.

I need Just harvest and Woodland covenant logos added.
Also to be added to the design is:
Single Origin
Traceability
Sustainability

"Awaken you senses" to be added.

I have added some jpegs that i own. you are free to use stock images where appropiate.

Target Market(s)

Coffee Consumers

Requirements
Must have
• Scalable vector files .. whatever images or file design you prodcue mut be able to be printed in high quality
High end quality
Awaken Your Senses needs tl be shown
Logos of just harvest or Wood land covenant to be added
200g weight to be shown
We have 4 beans which need to be shown individually
Velma Nectar
K3 Morandi
Teal Juniper
Altezza Amber
Nice to have
• You are welcome to come up with your own design

```html
<!DOCTYPE html>
<html lang="en">
<head>
<meta charset="UTF-8">
<title>Cafe de Marvela – Altezza Amber 200 gr</title>
<link rel="stylesheet" href="https://fonts.googleapis.com/css2?family=EB+Garamond:wght@400;500;600&display=swap">
<style>
  :root {
    --backdrop: #f6f5f3;
    --bag-black: #0b0b0b;
    --bag-edge: #1c1c1c;
    --gold: #d4ad3c;
    --gold-light: #f0d862;
    --gold-mid: #c99a1e;
    --gold-deep: #8a5a0c;
    --ink: #111111;
    --label-text: #e8e2d4;
    --leaf: #5f7356;
    --leaf-dark: #34473a;
    --berry: #9c3a3c;
    --anise: #6b3e22;
  }
  * { margin: 0; padding: 0; box-sizing: border-box; }
  html, body {
    width: 1167px;
    height: 1200px;
    overflow: hidden;
    background: var(--backdrop);
  }
  .canvas {
    position: relative;
    width: 1167px;
    height: 1200px;
    background: var(--backdrop);
    font-family: "EB Garamond", Georgia, serif;
  }
  .pack-front {
    position: absolute;
    left: 363px;
    top: 120px;
    width: 440px;
    height: 960px;
    background: var(--bag-black);
    border: 1px solid var(--bag-edge);
    overflow: hidden;
  }
  .botanical {
    position: absolute;
    border-radius: 48% 52% 46% 54%;
  }
  .botanical--top-right {
    right: -40px; top: 20px; width: 200px; height: 260px;
    background: radial-gradient(ellipse at 55% 35%, var(--berry) 0%, var(--leaf) 45%, rgba(52,71,58,0.6) 75%, transparent 100%);
  }
  .botanical--top-left {
    left: -30px; top: 170px; width: 110px; height: 280px;
    background: radial-gradient(ellipse at 55% 50%, #d9d6c8 0%, var(--leaf) 35%, rgba(52,71,58,0.7) 70%, transparent 100%);
  }
  .botanical--lower-left {
    left: -30px; top: 610px; width: 100px; height: 340px;
    background: radial-gradient(ellipse at 60% 60%, var(--leaf) 0%, var(--leaf-dark) 55%, transparent 100%);
  }
  .botanical--lower-right {
    right: -30px; top: 520px; width: 100px; height: 300px;
    background: radial-gradient(ellipse at 40% 50%, var(--leaf-dark) 0%, var(--leaf) 40%, rgba(156,58,60,0.5) 65%, transparent 100%);
  }
  .spice {
    position: absolute;
    width: 36px; height: 36px;
    border-radius: 50%;
    background: radial-gradient(circle, #8a5634 0%, var(--anise) 55%, transparent 75%);
  }
  .spice--a { left: 396px; top: 355px; }
  .spice--b { left: 400px; top: 408px; }
  .spice--c { left: 52px; top: 440px; }
  .spice--d { left: 20px; top: 478px; }

  .certifications {
    position: absolute;
    left: 28px;
    top: 36px;
    display: flex;
    gap: 12px;
  }
  .certifications__badge {
    width: 40px; height: 40px;
    border-radius: 50%;
    border: 2px solid var(--gold);
  }

  .brand-mark {
    position: absolute;
    left: 0; right: 0;
    top: 226px;
    display: flex;
    flex-direction: column;
    align-items: center;
    gap: 14px;
  }
  .brand-mark__circle {
    width: 64px; height: 64px;
    border-radius: 50%;
    border: 2px solid var(--gold);
  }
  .brand-mark__name {
    color: var(--gold);
    font-weight: 500;
    font-size: 26px;
    letter-spacing: 3px;
    text-transform: uppercase;
  }
  .tagline {
    position: absolute;
    left: 0; right: 0;
    top: 472px;
    text-align: center;
    color: var(--gold);
    font-weight: 500;
    font-size: 28px;
  }
  .product-label {
    position: absolute;
    left: 70px;
    top: 566px;
    width: 335px;
    height: 346px;
    background: linear-gradient(100deg, var(--gold-deep) 0%, var(--gold-mid) 30%, var(--gold-light) 55%, var(--gold-mid) 80%, var(--gold-deep) 100%);
    text-align: center;
  }
  .product-label__name {
    margin-top: 22px;
    color: var(--ink);
    font-weight: 500;
    font-size: 44px;
    line-height: 48px;
    text-transform: uppercase;
  }
  .product-label__panel {
    margin: 14px auto 0;
    width: 285px;
    height: 152px;
    background: var(--ink);
    outline: 2px solid var(--ink);
    outline-offset: 4px;
    display: flex;
    flex-direction: column;
    align-items: center;
    justify-content: center;
    gap: 14px;
  }
  .product-label__pillars {
    color: var(--label-text);
    font-size: 15px;
  }
  .product-label__rule {
    width: 90px; height: 2px;
    background: var(--gold);
  }
  .product-label__grade {
    color: var(--label-text);
    font-size: 17px;
    letter-spacing: 0.5px;
  }
  .product-label__weight {
    margin-top: 16px;
    color: var(--ink);
    font-size: 22px;
  }
</style>
</head>
<body>
<main class="canvas">
  <section class="pack-front">
    <div class="botanical botanical--top-right" role="img" aria-label="Watercolour coffee branch with leaves and red cherries"></div>
    <div class="botanical botanical--top-left" role="img" aria-label="Watercolour coffee leaves with white blossom and red cherries"></div>
    <div class="botanical botanical--lower-left" role="img" aria-label="Watercolour coffee leaves with white blossom"></div>
    <div class="botanical botanical--lower-right" role="img" aria-label="Watercolour coffee leaves and red cherries"></div>
    <div class="spice spice--a" role="img" aria-label="Star anise illustration"></div>
    <div class="spice spice--b" role="img" aria-label="Star anise illustration"></div>
    <div class="spice spice--c" role="img" aria-label="Star anise illustration"></div>
    <div class="spice spice--d" role="img" aria-label="Star anise illustration"></div>

    <div class="certifications">
      <span class="certifications__badge" role="img" aria-label="Just harvest certification badge"></span>
      <span class="certifications__badge" role="img" aria-label="Woodland covenant certification badge"></span>
    </div>

    <div class="brand-mark">
      <span class="brand-mark__circle"></span>
      <span class="brand-mark__name">Cafe de Marvela</span>
    </div>

    <p class="tagline">Awaken Your Senses</p>

    <div class="product-label">
      <h1 class="product-label__name">Altezza<br>Amber</h1>
      <div class="product-label__panel">
        <p class="product-label__pillars">Single Origin - Traceability - Sustainability</p>
        <span class="product-label__rule"></span>
        <p class="product-label__grade">HIGH END QUALITY</p>
      </div>
      <p class="product-label__weight">200 gr</p>
    </div>
  </section>
</main>
</body>
</html>
```